Business Card Design

We need a business card designed to portray the message that we are wedding and event stylists. We set up garden ceremonies and style wedding reception venues with chair covers and sashes, backdrops and draping's, wishing wells, tealight holders, table centerpieces. We also style corporate functions - Christmas parties, gala dinners, school formals, award nights. The colour of our uniforms are black and hot pink, if these colours could be incorporated. We would like to be able to use this design for letterhead, flyers and postcards etc. We would like the design to portray a professional, classic image that would relate to both spectrums of our business, weddings and corporate events. If you could develop a logo to incorporate would be great

Target Market(s)

brides, corporate compaines

Industry/Entity Type

Wedding

Contact Information for Business Card

Velvet Aisle & Function Rentals
Phone: 0413 586 190 Email:vaafr@quokkamail.com
Web: www.velvetaisleandfunctions.com.au

Requirements
Must have
• Must include that we set up for weddings, engagements, birthdays, anniversaries, corporate functions, school formals, any occasion.

```html
<!DOCTYPE html>
<html lang="en">
<head>
<meta charset="utf-8">
<title>Velvet Aisle and Function Rentals – Identity</title>
<link rel="stylesheet" href="https://fonts.googleapis.com/css2?family=Tinos:ital,wght@0,400;0,700;1,400;1,700&display=swap">
<style>
  :root {
    --paper: #ffffff;
    --card-light: #ffffff;
    --card-shade: #f1f1f1;
    --card-edge: #c9c9c9;
    --brand-brown: #6b4427;
    --rose: #b98a85;
    --rose-soft: #d9bcb8;
    --hairline: #eadbd8;
  }
  * { margin: 0; padding: 0; box-sizing: border-box; }
  html, body {
    width: 1200px; height: 1112px; overflow: hidden;
    background: var(--paper);
    font-family: "Tinos", "Times New Roman", serif;
  }
  .canvas { position: relative; width: 1200px; height: 1112px; }

  .ornament {
    position: absolute;
    border-radius: 50%;
    background: radial-gradient(ellipse at 45% 40%, var(--rose) 0%, var(--rose-soft) 55%, rgba(217,188,184,0) 75%);
  }
  .rule { position: absolute; height: 1px; background: var(--hairline); }

  .brand-name {
    position: absolute; white-space: nowrap;
    font-weight: 700; color: var(--brand-brown);
  }
  .brand-tagline {
    position: absolute; white-space: nowrap;
    color: var(--rose); letter-spacing: 0.14em;
  }

  /* standalone logo lockup */
  .logo-lockup .brand-name { left: 330px; top: 214px; font-size: 44px; }
  .logo-lockup .brand-tagline { left: 240px; top: 278px; font-size: 28px; }

  /* business card */
  .business-card {
    position: absolute; left: 170px; top: 440px; width: 864px; height: 528px;
    border: 1px solid var(--card-edge);
    background: linear-gradient(115deg, var(--card-shade) 0%, var(--card-light) 40%, var(--card-light) 70%, var(--card-shade) 100%);
    overflow: hidden;
  }
  .card-backdrop {
    position: absolute; left: 0; top: 0; width: 100%; height: 100%;
    background: radial-gradient(ellipse at 15% 35%, rgba(185,138,133,0.08) 0%, rgba(185,138,133,0) 45%),
                radial-gradient(ellipse at 90% 85%, rgba(185,138,133,0.06) 0%, rgba(185,138,133,0) 40%);
  }
  .business-card .brand-name { left: 240px; top: 133px; font-size: 33px; }
  .business-card .brand-tagline { left: 150px; top: 176px; font-size: 21px; }
  .services {
    position: absolute; left: 0; top: 266px; width: 100%;
    text-align: center; color: var(--brand-brown); font-size: 25px; line-height: 34px;
  }
  .contact-heading {
    position: absolute; left: 0; top: 374px; width: 100%;
    text-align: center; color: var(--brand-brown);
    font-size: 22px; font-weight: 700; font-style: italic;
  }
  .contact-details {
    position: absolute; left: 0; top: 420px; width: 100%;
    text-align: center; color: var(--rose); font-size: 27px; word-spacing: 2px;
  }
  .contact-details .email { margin-left: 32px; }
  .website {
    position: absolute; left: 0; top: 482px; width: 100%;
    text-align: center; color: var(--rose); font-size: 23px;
  }
</style>
</head>
<body>
<div class="canvas">

  <section class="logo-lockup">
    <div class="ornament" style="left:137px;top:94px;width:274px;height:197px;" role="img" aria-label="Floral flourish ornament in dusty rose"></div>
    <div class="rule" style="left:343px;top:199px;width:751px;"></div>
    <div class="brand-name">Velvet Aisle and Function Rentals</div>
    <div class="brand-tagline">Formally Velvet Weddings By Marguerite</div>
    <div class="ornament" style="left:986px;top:240px;width:108px;height:86px;" role="img" aria-label="Small floral sprig ornament in dusty rose"></div>
  </section>

  <section class="business-card">
    <div class="card-backdrop" role="img" aria-label="Faint floral pattern background"></div>
    <div class="ornament" style="left:79px;top:49px;width:197px;height:145px;" role="img" aria-label="Floral flourish ornament in dusty rose"></div>
    <div class="rule" style="left:199px;top:126px;width:591px;"></div>
    <div class="brand-name">Velvet Aisle and Function Rentals</div>
    <div class="brand-tagline">Formally Velvet Weddings By Marguerite</div>
    <div class="ornament" style="left:704px;top:168px;width:86px;height:52px;" role="img" aria-label="Small floral sprig ornament in dusty rose"></div>
    <div class="rule" style="left:113px;top:225px;width:574px;"></div>

    <div class="services">
      Weddings | Engagements | Birthdays | Anniversaries<br>
      Corporate Functions | School formals | Any Occasion
    </div>

    <div class="rule" style="left:156px;top:391px;width:190px;"></div>
    <div class="contact-heading">Contact Us at:</div>
    <div class="rule" style="left:518px;top:391px;width:190px;"></div>

    <div class="contact-details">
      <span class="phone">Phone: 0413 586 190</span><span class="email">Email:vaafr@quokkamail.com</span>
    </div>
    <div class="rule" style="left:216px;top:470px;width:432px;"></div>
    <div class="website">www.velvetaisleandfunctions.com.au</div>
  </section>

</div>
</body>
</html>
```